Flyer Photography modern, stylish classy

Edler and modern flyer makes people curious. 2 each representing my photographic activities generally. Appears to be: my logo, my address: Jonas Brehmer photographer in the house Wendelhof. . Kastanienweg 47 07319 Gera Tel (0361) 47 15 3 62 Email: Fotograf@JonasBrehmer-bild.eu Homepage: www.jonasbrehmer-bild.eu Note from 01.06.2016 is from "photo workshop 42" "Jonas Brehmer Photographer" with a new logo and a new location.
Updates

Project Deadline Extended Reason: Can not upload my full logo until 17.05.2016. Added Saturday, May 7, 2016

Target Market(s)

, To marry people aged 25 and over who are stylish and open-minded or simply want to have sophisticated images of themselves.

Font styles to use
Serif

Requirements
Must have
• Elegant and stylish look that makes one curious. It should radiate a valence and be modern. make to be photographed people like.
Nice to have
• The design of this general Flyers with the address data etc. (as described above) is can be applied to other topics-flyer like wedding, portrait - recognition.
Should not have
• loud colors

```html
<!DOCTYPE html>
<html lang="de">
<head>
<meta charset="utf-8">
<title>Jonas Brehmer Fotograf – Flyer</title>
<link rel="stylesheet" href="https://fonts.googleapis.com/css2?family=Merriweather:wght@300;700&display=swap">
<style>
  :root {
    --paper: #ffffff;
    --ink: #000000;
    --light: #ffffff;
    --wood-dark: #2a2016;
    --wood-mid: #6b5540;
    --wood-light: #a89580;
    --metal: #c9c3b4;
  }
  html, body {
    margin: 0;
    padding: 0;
    width: 1200px;
    height: 927px;
    overflow: hidden;
    background: var(--paper);
  }
  .flyer {
    position: relative;
    width: 1200px;
    height: 927px;
    background: var(--paper);
    font-family: "Merriweather", Georgia, serif;
    color: var(--light);
  }
  .brand-band {
    position: absolute;
    left: 0; top: 42px;
    width: 1200px; height: 245px;
    background: var(--ink);
  }
  .brand-mark {
    position: absolute;
    left: 548px; top: 72px;
    width: 96px; height: 96px;
    box-sizing: border-box;
    border: 3px solid var(--light);
    border-radius: 50%;
  }
  .brand-name {
    position: absolute;
    left: 0; top: 178px;
    width: 1200px;
    text-align: center;
    font-weight: 300;
    font-size: 36px;
    letter-spacing: 2px;
    text-transform: uppercase;
    line-height: 1;
    margin: 0;
  }
  .brand-role {
    position: absolute;
    left: 0; top: 228px;
    width: 1200px;
    text-align: center;
    font-weight: 300;
    font-size: 15px;
    letter-spacing: 7px;
    text-transform: uppercase;
    line-height: 1;
    margin: 0;
  }
  .hero {
    position: absolute;
    left: 0; top: 328px;
    width: 1200px; height: 381px;
    overflow: hidden;
  }
  .hero-photo {
    position: absolute;
    inset: 0;
    background:
      radial-gradient(ellipse 260px 170px at 700px 170px, rgba(215,205,185,0.75), rgba(215,205,185,0) 70%),
      radial-gradient(ellipse 200px 90px at 620px 270px, rgba(190,160,100,0.55), rgba(190,160,100,0) 70%),
      linear-gradient(160deg, var(--wood-dark) 0%, var(--wood-mid) 35%, var(--wood-light) 55%, var(--wood-mid) 75%, var(--wood-dark) 100%);
  }
  .hero-square {
    position: absolute;
    background: var(--light);
  }
  .hero-square--back  { left: 18px;  top: 19px;  width: 256px; height: 256px; opacity: 0.28; }
  .hero-square--mid   { left: 108px; top: 109px; width: 206px; height: 205px; opacity: 0.45; }
  .hero-square--front { left: 193px; top: 194px; width: 162px; height: 161px; opacity: 0.7; }
  .contact-band {
    position: absolute;
    left: 0; top: 709px;
    width: 1200px; height: 218px;
    background: var(--ink);
  }
  .contact {
    position: absolute;
    left: 60px; top: 44px;
    width: 1080px;
    margin: 0;
    text-align: center;
    font-weight: 300;
    font-size: 14.5px;
    line-height: 21.3px;
  }
  .contact strong { font-weight: 700; }
  .contact p { margin: 0; }
</style>
</head>
<body>
  <main class="flyer">
    <header class="brand-band">
      <div class="brand-mark"></div>
      <p class="brand-name">Jonas Brehmer</p>
      <p class="brand-role">Fotograf</p>
    </header>

    <section class="hero">
      <div class="hero-photo" role="img" aria-label="Nahaufnahme zweier Eheringe aus Silber und Gold mit Gravur auf verwittertem Holz im Sonnenlicht"></div>
      <div class="hero-square hero-square--back"></div>
      <div class="hero-square hero-square--mid"></div>
      <div class="hero-square hero-square--front"></div>
    </section>

    <footer class="contact-band">
      <div class="contact">
        <p><strong>Meine Anschrift:</strong> Jonas Brehmer Fotograf im Haus Wendelhof. Kastanienweg 47 07319 Gera</p>
        <p><strong>Tel.</strong> (0361) 47 15 3 62</p>
        <p><strong>Email:</strong> Fotograf@JonasBrehmer-bild.eu</p>
        <p><strong>Homepage:</strong> www.jonasbrehmer-bild.eu</p>
        <p><strong>Wichtiger Hinweis:</strong> Ich ziehe mit meinem Fotostudio am 01.06.2016 in eine andere Location und werde auch ein neues Logo haben -aus<br>" photo workshop 42 " " Jonas Brehmer Fotograf "</p>
      </div>
    </footer>
  </main>
</body>
</html>
```